GearVinto is a company based in dubai that acts as a market place for the automotive industry

from a b2c prospective our company acts as a marketplace that offers :

*booking services for car workshops whereas users can find nearest car workshop and book desired services.
* review, rate, the workshop once service i complete.
*pickup and drop off services (offered from the workshop).
*inspection services (offered from the workshop).
_______________________________________

*users can display or view a car to sell or buy.

*online merchant store for (parts, accessories, gadgets).
________________________________________

- a live customer service feature in the website.
- signing up options.

Target Market(s)

three target segments:
- customers that need to fix their cars.
- car workshop owners
-merchants
-people that want to buy/sell their car

Industry/Entity Type

Automotive

Contact Information for Business Card

frontside: name, email, landline number, mobile number, location, social media
back side: only logo

Logo Text

Gearvinto

Number of Pages Required

3 page

Font styles to use
Other font styles liked:
• Dubai font

```html
<!DOCTYPE html>
<html lang="en">
<head>
<meta charset="utf-8">
<title>MotorAke – Automotive Marketplace</title>
<link href="https://fonts.googleapis.com/css2?family=Arimo:wght@400;700&family=Cormorant+Garamond:wght@500&family=Open+Sans:wght@400;600;700&display=swap" rel="stylesheet">
<style>
:root{
  --red:#d9464f;
  --red-dark:#c13a43;
  --red-deep:#b8323b;
  --ink:#222;
  --muted:#777;
  --dark:#2b2d33;
  --panel:#25272d;
  --field:#35373e;
  --light:#f2f3f5;
  --link:#3a5bb8;
  --white:#fff;
}
*{box-sizing:border-box;margin:0;padding:0}
html,body{width:1200px;height:3659px;overflow:hidden}
body{font-family:"Open Sans",Arial,sans-serif;color:var(--ink);background:var(--white);position:relative}
.topbar{height:48px;background:var(--dark);color:#ddd;font-size:13px;display:flex;align-items:center;padding:0 68px;gap:40px}
.topbar .item{display:flex;align-items:center;gap:10px}
.topbar .social{margin-left:auto;display:flex;gap:12px}
.dot{width:12px;height:12px;border-radius:50%;background:#7d8088;display:inline-block}
.header{height:167px;display:flex;align-items:center;padding:0 68px}
.brand{display:flex;align-items:center;gap:12px;font-family:"Arimo",sans-serif;font-weight:700;font-size:30px;color:var(--ink)}
.brand .mark{width:28px;height:28px;background:var(--ink)}
.contacts{margin-left:auto;display:flex;gap:70px}
.contact{display:flex;gap:16px;align-items:center;font-size:14px}
.contact b{display:block;font-weight:600;color:#333}
.contact span{color:var(--muted);font-size:13px}
.nav{height:65px;background:var(--red);display:flex;align-items:center;padding:0 68px;gap:38px;color:var(--white);font-size:16px;font-family:"Arimo",sans-serif}
.nav .cart{margin-left:auto;width:60px;height:65px;background:var(--red-dark);display:flex;align-items:center;justify-content:center}
.hero{height:610px;position:relative;background:linear-gradient(180deg,#c8c2b8 0%,#8e877d 45%,#3e3c3a 100%)}
.hero h1{position:absolute;top:195px;left:0;right:0;text-align:center;font-family:"Cormorant Garamond",serif;font-weight:500;font-size:78px;line-height:84px;color:var(--white)}
.search{position:absolute;left:68px;top:508px;width:1067px;z-index:2}
.tabs{display:flex;height:62px}
.tab{background:var(--dark);color:#fff;font-size:15px;font-weight:600;display:flex;align-items:center;justify-content:center;border-right:1px solid #444}
.tab.active{background:var(--panel)}
.fields{background:var(--panel);height:95px;display:flex;align-items:center;padding:0 32px;gap:32px}
.field{background:var(--field);color:#999;font-size:12px;height:42px;width:150px;display:flex;align-items:center;justify-content:center}
.btn-search{margin-left:auto;background:var(--red);color:#fff;font-weight:700;font-size:15px;width:180px;height:42px;display:flex;align-items:center;justify-content:center}
.welcome{padding:124px 68px 0;display:flex;gap:100px}
.welcome h2{font-family:"Arimo",sans-serif;font-weight:400;font-size:50px;line-height:58px;width:360px}
.welcome p{font-family:"Arimo",sans-serif;font-size:21px;line-height:30px;color:var(--muted);width:640px}
.features{display:flex;gap:28px;padding:42px 68px 0}
.feature{width:245px}
.feature .img{height:170px}
.feature h3{font-family:"Arimo",sans-serif;font-weight:400;font-size:21px;margin:40px 0 14px}
.feature p{font-size:12px;line-height:20px;color:var(--muted)}
.feature a{display:block;margin-top:16px;font-size:12px;color:var(--link);text-decoration:none}
.offers{position:absolute;top:1527px;left:0;width:1200px;height:308px;display:flex;background:var(--red)}
.offer{flex:1;padding:50px 40px 0 90px;color:var(--white);position:relative}
.offer.mid{background:var(--red-deep)}
.offer svg{position:absolute;left:30px;top:48px}
.offer h4{font-size:17px;font-weight:700;margin-bottom:16px}
.offer p{font-size:13px;line-height:22px;width:270px}
.offer .btn{display:inline-block;margin-top:24px;background:var(--dark);font-size:12px;font-weight:700;padding:10px 28px}
.products{position:absolute;top:1835px;left:0;width:1200px;height:655px;background:var(--light);text-align:center}
.products h2,.reviews h2{font-family:"Arimo",sans-serif;font-weight:400;font-size:40px}
.products h2{margin-top:62px}
.products .sub{font-size:13px;color:var(--muted);margin-top:26px;letter-spacing:.5px}
.grid{display:flex;gap:31px;justify-content:center;margin-top:64px}
.product{width:240px;height:341px;background:var(--white)}
.product .img{height:248px;background:var(--white);display:flex;align-items:center;justify-content:center}
.product .img div{width:140px;height:140px;border-radius:50%;background:radial-gradient(#bfc2c6,#8a8d92)}
.product.hover .img{background:#55575d;position:relative}
.product.hover .img div{background:radial-gradient(#777,#444)}
.hover .cartbtn{position:absolute;left:50px;top:95px;background:#3a3c42;color:#fff;font-size:13px;display:flex;height:38px;align-items:center}
.hover .cartbtn span{padding:0 14px}
.hover .cartbtn i{width:40px;height:38px;background:var(--red);display:block}
.product .name{font-size:14px;margin-top:22px;color:#444}
.product .price{font-size:15px;font-weight:700;color:var(--red);margin-top:4px}
.dots{display:flex;gap:8px;justify-content:center;margin-top:34px}
.dots i{width:8px;height:8px;border-radius:50%;background:#ccc}
.dots i:first-child{background:var(--red)}
.reviews{position:absolute;top:2490px;left:0;width:1200px;height:760px;text-align:center}
.reviews h2{margin-top:46px}
.reviews .sub{font-size:14px;color:var(--muted);margin-top:20px}
.review{position:absolute;text-align:left;color:var(--white)}
.review.big{left:68px;top:152px;width:701px;height:476px;background:linear-gradient(180deg,#6f6a5b 0%,#3b3c38 55%,#151617 100%)}
.review.small1{left:798px;top:152px;width:334px;height:226px;background:linear-gradient(180deg,#5f7ea3,#43526a)}
.review.small2{left:798px;top:402px;width:334px;height:226px;background:linear-gradient(180deg,#8a8e88,#4b4e4c)}
.rating{position:absolute;top:20px;right:20px;background:var(--red);width:64px;height:70px;text-align:center;font-weight:700;font-size:26px;padding-top:10px}
.rating small{display:block;font-size:9px}
.small1 .rating,.small2 .rating{width:52px;height:56px;font-size:21px;padding-top:6px;top:16px;right:16px}
.review .info{position:absolute;left:20px;bottom:22px;right:20px}
.review .date{font-size:11px;opacity:.8}
.review h5{font-size:22px;font-weight:700;margin:6px 0 10px}
.small1 h5,.small2 h5{font-size:14px;margin:4px 0 0}
.review p{font-size:12px;line-height:20px}
.review p span{color:#7fa0ff}
.more{position:absolute;left:520px;top:670px;width:163px;height:40px;background:#d8d9db;color:#555;font-size:13px;display:flex;align-items:center;justify-content:center}
.footer{position:absolute;top:3250px;left:0;width:1200px;height:409px;background:var(--dark);color:#bbb;font-size:12px}
.cols{display:flex;padding:66px 115px 0;gap:0}
.col{width:250px;line-height:22px}
.col h6{font-size:14px;color:#fff;font-weight:600;margin-bottom:26px}
.col .red{color:var(--red)}
.col .gap{margin-top:28px}
.col .social{display:flex;gap:16px;margin-bottom:36px}
.newsletter{display:flex;margin-top:8px}
.newsletter div{width:170px;height:38px;background:#fff;color:#555;font-size:11px;display:flex;align-items:center;padding-left:10px}
.newsletter i{width:42px;height:38px;background:#3a3c42;display:block}
.copyright{position:absolute;left:0;right:0;bottom:0;height:58px;border-top:1px solid #3c3e45;text-align:center;line-height:58px;color:#ddd}
</style>
</head>
<body>
<div class="topbar">
  <div class="item"><svg width="14" height="14" viewBox="0 0 14 14"><circle cx="7" cy="4" r="3" fill="#ddd"/><path d="M1 14c0-4 3-6 6-6s6 2 6 6z" fill="#ddd"/></svg>Signing Up</div>
  <div class="item"><svg width="14" height="14" viewBox="0 0 14 14"><circle cx="6" cy="6" r="4.5" fill="none" stroke="#ddd" stroke-width="2"/><path d="M9 9l4 4" stroke="#ddd" stroke-width="2"/></svg>Search</div>
  <div class="social"><i class="dot"></i><i class="dot"></i><i class="dot"></i><i class="dot"></i><i class="dot"></i><i class="dot"></i></div>
</div>

<header class="header">
  <div class="brand"><span class="mark"></span>MotorAke</div>
  <div class="contacts">
    <div class="contact"><svg width="30" height="30" viewBox="0 0 30 30"><rect x="3" y="5" width="24" height="22" fill="none" stroke="#d9464f" stroke-width="2.5"/><path d="M3 11h24M10 2v6M20 2v6" stroke="#d9464f" stroke-width="2.5"/></svg><div><b>Mon - Sat: 9:00am - 5:00pm</b><span>Sunday Closed</span></div></div>
    <div class="contact"><svg width="24" height="32" viewBox="0 0 24 32"><path d="M12 2a10 10 0 0 0-10 10c0 8 10 18 10 18s10-10 10-18A10 10 0 0 0 12 2z" fill="none" stroke="#d9464f" stroke-width="2.5"/><circle cx="12" cy="12" r="4" fill="#d9464f"/></svg><div><b>18 Harbor Lane</b><span>Lakeview</span></div></div>
    <div class="contact"><svg width="20" height="32" viewBox="0 0 20 32"><rect x="2" y="2" width="16" height="28" rx="3" fill="none" stroke="#d9464f" stroke-width="2.5"/><path d="M7 25h6" stroke="#d9464f" stroke-width="2.5"/></svg><div><b>+00 1234 0000</b><span>hello@motorake.com</span></div></div>
  </div>
</header>

<nav class="nav">
  <span>HOME</span><span>ABOUT US</span><span>SERVICES</span><span>CAR WORKSHOP</span><span>SELL</span><span>BUY</span><span>STORE</span><span>CONTACT</span>
  <span class="cart"><svg width="26" height="22" viewBox="0 0 26 22"><path d="M1 2h4l3 12h13l3-9H7" fill="none" stroke="#fff" stroke-width="2"/><circle cx="10" cy="19" r="2" fill="#fff"/><circle cx="19" cy="19" r="2" fill="#fff"/></svg></span>
</nav>

<section class="hero" role="img" aria-label="Dark sports SUV parked by a city waterfront at sunset">
  <h1>Best Place To Services<br>For Your Vehicle!</h1>
  <div class="search">
    <div class="tabs">
      <div class="tab active" style="width:130px">Sell</div>
      <div class="tab" style="width:120px">Buy</div>
      <div class="tab" style="width:200px">Car Workshop</div>
      <div class="tab" style="width:240px">Service Center &amp; Dealer</div>
    </div>
    <div class="fields">
      <div class="field">All Makes ⌄</div><div class="field">All Models ⌄</div><div class="field">Max Price ⌄</div><div class="field">2000Km ⌄</div><div class="field">Lakeview City ⌄</div>
      <div class="btn-search">SEARCH</div>
    </div>
  </div>
</section>

<section class="welcome">
  <h2>Welcome to MotorAke</h2>
  <p>Aenean auctor wisi et urna. Aliquam erat volutpat. Duis ac turpis. Integer rutrum ante eu lacus. Vestibulum libero nisl, porta vel, scelerisque eget, malesuada at, neque.</p>
</section>

<section class="features">
  <div class="feature"><div class="img" role="img" aria-label="Rows of new and used cars in a showroom" style="background:linear-gradient(#dfe3e8,#8d949c)"></div><h3>New &amp; Used Vehicles</h3><p>Mauris fermentum dictum magna. Sed laoreet aliquam leo. Ut tellus dolor, dapibus eget, elementum vel.</p><a>View Inventory »</a></div>
  <div class="feature"><div class="img" role="img" aria-label="Car interior with steering wheel and dashboard" style="background:linear-gradient(#cfcfcf,#6b6b6b)"></div><h3>Research &amp; Reviews</h3><p>Aenean auctor wisi et urna. Aliquam erat volutpat. Duis ac turpis. Integer rutrum ante eu lacus Vestibulum libero nisl.</p><a>See Research &amp; Reviews »</a></div>
  <div class="feature"><div class="img" role="img" aria-label="Mechanic in a workshop" style="background:linear-gradient(#e6d9c8,#8e7b66)"></div><h3>Service &amp; Repair</h3><p>Mauris fermentum dictum magna. Sed laoreet aliquam leo. Ut tellus dolor, dapibus eget, elementum vel.</p><a>Schedule Now »</a></div>
  <div class="feature"><div class="img" role="img" aria-label="Family receiving car keys at a dealership" style="background:linear-gradient(#e9d3d0,#a05d5a)"></div><h3>Stress Free Financing</h3><p>Mauris fermentum dictum magna. Sed laoreet aliquam leo. Ut tellus dolor, dapibus eget, elementum vel.</p><a>Read More »</a></div>
</section>

<section class="offers">
  <div class="offer"><svg width="40" height="40" viewBox="0 0 40 40"><circle cx="16" cy="16" r="11" fill="none" stroke="#fff" stroke-width="3"/><path d="M24 24l12 12" stroke="#fff" stroke-width="3"/></svg><h4>Looking For Buy a Car?</h4><p>Now is a good time to buy a car, Engines provide you new and used car in good conditions, after full car checkup only we deleverd your car to you with fully completed documentations.</p><span class="btn">BUY A CAR</span></div>
  <div class="offer mid"><svg width="40" height="40" viewBox="0 0 40 40"><path d="M4 26l4-10h22l4 10v6H4z" fill="#fff"/><circle cx="11" cy="32" r="3" fill="#b8323b"/><circle cx="28" cy="32" r="3" fill="#b8323b"/><circle cx="26" cy="9" r="6" fill="#fff"/></svg><h4>Do You Want to Sell a Car?</h4><p>Now is a good time to buy a car, Engines provide you new and used car in good conditions, after full car checkup only we deleverd your car to you with fully completed documentations.</p><span class="btn">SELL A CAR</span></div>
  <div class="offer"><svg width="40" height="40" viewBox="0 0 40 40"><circle cx="12" cy="8" r="5" fill="#fff"/><circle cx="28" cy="8" r="5" fill="#fff"/><rect x="6" y="15" width="12" height="22" fill="#fff"/><rect x="22" y="15" width="12" height="22" fill="#fff"/></svg><h4>Kids Grill the Car Experts</h4><p>Now is a good time to buy a car, Engines provide you new and used car in good conditions, after full car checkup only we deleverd your car to you with fully completed documentations.</p><span class="btn">KNOW MORE</span></div>
</section>

<section class="products">
  <h2>Our Products</h2>
  <p class="sub">Phasellus imperdiet libero sit amet ante Donec convallis elementum leum</p>
  <div class="grid">
    <div class="product"><div class="img" role="img" aria-label="Car starter motor"><div></div></div><p class="name">Car Accessories</p><p class="price">$ 1500</p></div>
    <div class="product hover"><div class="img" role="img" aria-label="Engine part shown with add to cart overlay"><div></div><span class="cartbtn"><span>Add to cart</span><i></i></span></div><p class="name">Car Accessories</p><p class="price">$ 1500</p></div>
    <div class="product"><div class="img" role="img" aria-label="Alloy wheel rim"><div></div></div><p class="name">Car Accessories</p><p class="price">$ 1500</p></div>
    <div class="product"><div class="img" role="img" aria-label="Brake disc with red caliper"><div></div></div><p class="name">Car Accessories</p><p class="price">$ 1500</p></div>
  </div>
  <div class="dots"><i></i><i></i></div>
</section>

<section class="reviews">
  <h2>Review, Rate, The Workshop</h2>
  <p class="sub">Our expert reviewers report back with the latest.</p>
  <article class="review big" role="img" aria-label="Dark saloon car on a tree-lined road">
    <div class="rating">4.5<small>OUT OF 5</small></div>
    <div class="info"><p class="date">OCTOBER 28, 2018</p><h5>Aliquam Dapibus Tincidunt Metus</h5><p>Aenean auctor wisi et urna. Aliquam erat volutpat. Duis ac turpis. Integer rutrum ante eu lacus. Vestibulum libero nisl, porta vel, scelerisque eget. <span>Read More »</span></p></div>
  </article>
  <article class="review small1" role="img" aria-label="Blue hatchback driving on a coastal road">
    <div class="rating">4.9<small>OUT OF 5</small></div>
    <div class="info"><p class="date">OCTOBER 28, 2018</p><h5>Mauris Fermentum Dictum Magna</h5></div>
  </article>
  <article class="review small2" role="img" aria-label="Grey off-road SUV on a mountain road">
    <div class="rating">3.2<small>OUT OF 5</small></div>
    <div class="info"><p class="date">OCTOBER 14, 2018</p><h5>Mauris Fermentum Dictum Magna</h5></div>
  </article>
  <div class="more">MORE REVIEWS</div>
</section>

<footer class="footer">
  <div class="cols">
    <div class="col"><h6>Contact Us</h6><p>MotorAke Office<br>22 Elm Row, Westbrook,<br>WB10 4QT</p><p class="gap">Phone: 800 555 0135<br>FAX: 800 555 0188<br>E-mail: <span class="red">mail@motorake.com</span></p></div>
    <div class="col"><h6>Opening Hours</h6><p>SALES:</p><p class="gap">Mon - Sat 9:00 AM - 6:00 PM<br>Sunday is closed</p><p class="gap">SERVICE:</p><p>Mon - Sat 9:00 AM - 6:00 PM<br>Sunday is closed</p></div>
    <div class="col red"><h6>Services</h6><p>New Cars For Sale<br>Pre-owned Cars<br>Sell My Car<br>Car Valuations<br>Financing &amp; Insurance<br>Service &amp; Repair</p></div>
    <div class="col"><h6>Connect With Us</h6><div class="social"><i class="dot"></i><i class="dot"></i><i class="dot"></i><i class="dot"></i><i class="dot"></i><i class="dot"></i></div><h6>Newsletter Sign Up</h6><div class="newsletter"><div>Enter your email address</div><i></i></div></div>
  </div>
  <div class="copyright">Copyright MotorAke © 2017. All Rights Reserved.</div>
</footer>
</body>
</html>
```